Business card based on your logo design "Brennock&Co"

Can you please design a business card based on the logo artwork you designed for our business. Double sided as per your submitted image of possible application of logo.

```html
<!DOCTYPE html>
<html lang="en">
<head>
<meta charset="utf-8">
<title>Brennock&amp;Co — Business Card</title>
<link rel="stylesheet" href="https://fonts.googleapis.com/css2?family=Jura:wght@400;600;700&display=swap">
<style>
  :root {
    --backdrop: #b9b9b9;
    --card-white: #fbfbfb;
    --brand-orange: #ef8a1d;
    --ink-dark: #2f2f31;
    --card-shadow: rgba(0, 0, 0, 0.22);
  }
  * { box-sizing: border-box; margin: 0; padding: 0; }
  html, body {
    width: 1200px;
    height: 960px;
    overflow: hidden;
  }
  body {
    background: var(--backdrop);
    font-family: "Jura", sans-serif;
    position: relative;
  }
  .card {
    position: absolute;
    width: 580px;
    height: 330px;
    background: var(--card-white);
    border-radius: 4px;
    box-shadow: 0 14px 30px var(--card-shadow);
    overflow: hidden;
  }

  /* Back side: name + contact details */
  .card--back { left: 470px; top: 110px; }
  .card--back .contact-band {
    position: absolute;
    left: 0; right: 0; bottom: 0;
    height: 205px;
    background: var(--brand-orange);
  }
  .card--back .holder {
    position: absolute;
    right: 58px;
    top: 52px;
    text-align: center;
  }
  .holder__name {
    font-size: 34px;
    font-weight: 400;
    letter-spacing: 3px;
    color: var(--ink-dark);
    line-height: 1;
  }
  .holder__role {
    font-size: 17px;
    letter-spacing: 2px;
    color: var(--brand-orange);
    margin-top: 4px;
  }
  .contact-list {
    position: absolute;
    left: 44px;
    top: 148px;
    list-style: none;
    color: var(--ink-dark);
    font-size: 17px;
    font-weight: 600;
    letter-spacing: 1.2px;
  }
  .contact-list li {
    display: flex;
    align-items: center;
    gap: 10px;
    height: 34px;
  }
  .contact-list svg {
    width: 18px;
    height: 18px;
    flex: none;
    fill: none;
    stroke: var(--card-white);
    stroke-width: 1.8;
    stroke-linecap: round;
    stroke-linejoin: round;
  }

  /* Front side: company name */
  .card--front {
    left: 150px;
    top: 520px;
    display: flex;
    flex-direction: column;
    align-items: center;
    justify-content: center;
  }
  .wordmark {
    display: flex;
    align-items: center;
    gap: 14px;
  }
  .wordmark__square {
    width: 22px;
    height: 22px;
    background: var(--brand-orange);
  }
  .wordmark__name {
    font-size: 58px;
    font-weight: 700;
    color: var(--ink-dark);
    letter-spacing: 1px;
    line-height: 1;
  }
  .tagline {
    margin-top: 14px;
    font-size: 15px;
    font-weight: 600;
    letter-spacing: 2.5px;
    color: var(--ink-dark);
  }
</style>
</head>
<body>

  <section class="card card--back" aria-label="Business card back">
    <div class="contact-band"></div>
    <div class="holder">
      <p class="holder__name">Martin Hale</p>
      <p class="holder__role">director</p>
    </div>
    <ul class="contact-list">
      <li>
        <svg viewBox="0 0 20 20"><path d="M2 10 L10 3 L18 10"/><path d="M4.5 8.5 V17 H15.5 V8.5"/><path d="M8.5 17 V12 H11.5 V17"/></svg>
        Harbour Lane 48, Boston 02110, U.S.A
      </li>
      <li>
        <svg viewBox="0 0 20 20"><path d="M5 2.5 L8 6 L6.5 8 C7.5 10.5 9.5 12.5 12 13.5 L14 12 L17.5 15 L15.5 17.5 C9 17 3 11 2.5 4.5 Z"/></svg>
        +0198 765 432
      </li>
      <li>
        <svg viewBox="0 0 20 20"><rect x="2.5" y="4.5" width="15" height="11" rx="1"/><path d="M2.5 5 L10 11 L17.5 5"/></svg>
        info@brennock.com
      </li>
      <li>
        <svg viewBox="0 0 20 20"><circle cx="10" cy="10" r="3"/><path d="M13 7 V11.5 C13 13.5 16.5 13.5 16.5 10 A6.5 6.5 0 1 0 13 15.8"/></svg>
        www.brennockandco.com
      </li>
    </ul>
  </section>

  <section class="card card--front" aria-label="Business card front">
    <div class="wordmark">
      <span class="wordmark__square" aria-hidden="true"></span>
      <h1 class="wordmark__name">Brennock&amp;Co</h1>
    </div>
    <p class="tagline">Building and Project Management</p>
  </section>

</body>
</html>
```